Packaging design for a low carb bar

I am producing a low carb / high fat bar, therefore I would like to have a light weighted modern design. The background color pastel light or something like that. The package should be focused on fitness-active individuals who are looking for healthy low carb snacks. Preliminary packaging size, logo, and more details on what should be attached to the packaging are attached. Thank you!

```html
<!DOCTYPE html>
<html lang="en">
<head>
<meta charset="utf-8">
<title>Northleaf Keto Bar – Almond Wrapper</title>
<link rel="stylesheet" href="https://fonts.googleapis.com/css2?family=Questrial&family=Raleway:wght@400;500&display=swap">
<style>
  :root {
    --teal: #2f93a6;
    --teal-pale: #c9e2e7;
    --ink: #3a3d40;
    --paper: #f6f6f6;
    --paper-warm: #efeae6;
    --photo-dark: #2c4a4f;
    --photo-mid: #6c8688;
    --photo-wood: #5a4a3e;
  }
  html, body {
    margin: 0;
    padding: 0;
    overflow: hidden;
    background: #ffffff;
  }
  .wrapper {
    position: relative;
    width: 1200px;
    height: 276px;
    overflow: hidden;
    background: linear-gradient(90deg, var(--paper) 0%, #fafafa 55%, var(--paper-warm) 100%);
    font-family: "Questrial", "Century Gothic", sans-serif;
  }
  .side-band {
    position: absolute;
    left: 0; top: 0;
    width: 133px; height: 276px;
    background: var(--teal);
  }
  .product-photo {
    position: absolute;
    left: 133px; top: 0;
    width: 340px; height: 276px;
    background:
      radial-gradient(ellipse at 55% 45%, var(--photo-mid) 0%, var(--photo-dark) 55%, transparent 80%),
      linear-gradient(160deg, var(--photo-dark) 0%, var(--photo-wood) 100%);
  }
  .halftone-edge {
    position: absolute;
    left: 470px; top: 0;
    width: 46px; height: 276px;
    background: linear-gradient(90deg, var(--photo-dark) 0%, #7e9699 45%, rgba(246,246,246,0) 100%);
  }
  .flavour {
    position: absolute;
    left: 538px; top: 26px;
    height: 224px;
    margin: 0;
    writing-mode: vertical-rl;
    transform: rotate(180deg);
    font-family: "Raleway", sans-serif;
    font-weight: 500;
    font-size: 44px;
    letter-spacing: 3px;
    color: var(--teal);
    text-align: center;
    line-height: 1;
  }
  .brand {
    position: absolute;
    left: 746px; top: 6px;
    width: 162px; height: 162px;
  }
  .brand-disc {
    position: absolute;
    inset: 0;
    border-radius: 50%;
    background: var(--teal-pale);
  }
  .brand-name {
    position: absolute;
    left: 0; right: 0; top: 64px;
    text-align: center;
    font-size: 28px;
    letter-spacing: 1px;
    color: #ffffff;
  }
  .product-name {
    position: absolute;
    left: 700px; top: 174px;
    width: 254px;
    margin: 0;
    text-align: center;
    font-weight: 400;
    font-size: 37px;
    line-height: 1;
    color: var(--ink);
  }
  .product-name .accent { color: var(--teal); }
  .claims {
    position: absolute;
    left: 692px; top: 222px;
    display: flex;
    align-items: stretch;
    font-size: 13.5px;
    line-height: 19px;
    color: var(--ink);
    white-space: nowrap;
  }
  .claim { padding: 0 12px; }
  .claim:first-child { padding-left: 0; }
  .claim + .claim { border-left: 2px solid var(--teal); }
  .ingredients {
    position: absolute;
    left: 1094px; top: 244px;
    width: 200px;
    transform-origin: 0 0;
    transform: rotate(-90deg);
  }
  .ingredients-title {
    margin: 0;
    font-family: "Raleway", sans-serif;
    font-weight: 400;
    font-size: 25px;
    letter-spacing: 0.5px;
    color: var(--teal);
    line-height: 28px;
    white-space: nowrap;
  }
  .ingredients-list {
    margin: 2px 0 0;
    font-size: 13px;
    line-height: 15px;
    color: var(--ink);
    white-space: nowrap;
  }
</style>
</head>
<body>
  <main class="wrapper">
    <div class="side-band"></div>
    <div class="product-photo" role="img" aria-label="Photograph of whole almonds spilling from a wooden scoop onto a rustic table"></div>
    <div class="halftone-edge" role="img" aria-label="Halftone dot transition from photo to label background"></div>

    <div class="flavour">ALMOND</div>

    <div class="brand">
      <div class="brand-disc"></div>
      <div class="brand-name">Northleaf</div>
    </div>

    <h1 class="product-name"><span class="accent">KETO</span> BAR</h1>

    <div class="claims">
      <div class="claim">Suitable for a<br>Keto / Lchf Diet</div>
      <div class="claim">3.5g Net<br>Carbs</div>
      <div class="claim">Vegan</div>
    </div>

    <section class="ingredients">
      <h2 class="ingredients-title">INGREDIENTS</h2>
      <p class="ingredients-list">Peanuts, Almonds, Chia,<br>Coconut Sunflower &amp;<br>Pumpkin Seeds.</p>
    </section>
  </main>
</body>
</html>
```